Postcard Design

We are Professional, quick and efficient. We are State Licensed and Insured. Gas•Water•Sewer Specializing in all of the customers plumbing needs. We accept credit cards. The law in Louisiana is that I have company address, and license number on all advertising. License number is RKT 4291. Address is 52907 north elm ave. Cut Off, La. 70218

```html
<!DOCTYPE html>
<html lang="en">
<head>
<meta charset="utf-8">
<title>Marcotte Plumbing Postcard</title>
<link rel="stylesheet" href="https://fonts.googleapis.com/css2?family=Poppins:ital,wght@0,400;0,600;0,800;1,400&family=Tinos:ital,wght@0,700;1,400&family=Comic+Neue:wght@700&display=swap">
<style>
  :root {
    --sky-top: #1b5da6;
    --sky-bottom: #4a93d6;
    --navy: #1f2f7a;
    --navy-deep: #16215c;
    --red: #c8202a;
    --red-bright: #e2232b;
    --yellow: #ffe600;
    --white: #ffffff;
    --steel: #b9bec4;
    --steel-dark: #6f767e;
    --scene-light: #dde6ee;
    --scene-mid: #9fb1c2;
  }
  * { margin: 0; padding: 0; box-sizing: border-box; }
  html, body { width: 1200px; height: 750px; overflow: hidden; background: #e9e9e9; }
  .postcard {
    position: relative; width: 1200px; height: 750px; overflow: hidden;
    background: linear-gradient(180deg, var(--sky-top) 0%, var(--sky-bottom) 32%, var(--white) 55%);
    font-family: "Poppins", sans-serif; color: var(--white);
  }
  .layer { position: absolute; }
  .backdrop-scene {
    left: 560px; top: 330px; width: 640px; height: 200px;
    background: linear-gradient(135deg, var(--scene-light), var(--scene-mid));
  }
  .promo-band { left: 0; top: 0; width: 1200px; height: 750px; }
  .faucet {
    left: 210px; top: 0; width: 170px; height: 175px;
    background: linear-gradient(90deg, var(--steel-dark), var(--steel) 45%, var(--steel-dark));
    border-radius: 0 0 60px 60px;
  }
  .brand { left: 420px; top: 32px; }
  .brand-name { font-weight: 800; font-size: 64px; line-height: 1; letter-spacing: 1px; }
  .brand-tagline { font-size: 24px; font-weight: 400; margin-top: 14px; letter-spacing: 1px; }
  .promo-copy {
    left: 140px; top: 200px; font-size: 19px; font-weight: 600; line-height: 1.35; letter-spacing: .5px;
  }
  .promo-copy .highlight { color: var(--red-bright); text-transform: uppercase; font-weight: 800; }
  .services { left: 118px; top: 318px; display: flex; gap: 24px; }
  .service {
    width: 106px; height: 106px; border-radius: 50%; border: 4px solid var(--navy);
    background: var(--white); position: relative; overflow: hidden;
  }
  .service-image { position: absolute; inset: 8px 8px 34px; border-radius: 50% 50% 20% 20%; }
  .service-label {
    position: absolute; left: 0; right: 0; bottom: 8px; text-align: center;
    font-family: "Comic Neue", cursive; font-weight: 700; font-size: 13px; line-height: 1;
    color: var(--navy); text-transform: uppercase;
  }
  .red-band { left: 0; top: 455px; width: 1200px; height: 295px; background: var(--red); }
  .plumber {
    left: 790px; top: 170px; width: 410px; height: 440px;
    background: linear-gradient(180deg, #2b3f80 0%, #223371 60%, #1a2a60 100%);
    border-radius: 180px 0 0 0;
  }
  .burst { left: 630px; top: 260px; width: 220px; height: 150px; }
  .burst-text {
    left: 630px; top: 303px; width: 220px; text-align: center;
    font-weight: 800; font-size: 20px; line-height: 1.05; text-transform: uppercase;
  }
  .headline { left: 70px; top: 478px; font-family: "Tinos", serif; }
  .headline-main { font-weight: 700; font-size: 58px; line-height: 1; }
  .headline-sub { font-style: italic; font-size: 44px; margin-left: 80px; line-height: 1.1; }
  .license {
    left: 820px; top: 500px; width: 350px; text-align: right;
    font-weight: 800; font-size: 27px; line-height: 1.1;
  }
  .contact { left: 560px; top: 600px; }
  .contact-phone { color: var(--yellow); font-weight: 800; font-size: 62px; line-height: 1; }
  .contact-address { font-size: 26px; margin-top: 10px; }
</style>
</head>
<body>
<main class="postcard">
  <div class="layer backdrop-scene" role="img" aria-label="Photo of pipes and plumbing fittings under a sink"></div>

  <svg class="layer promo-band" viewBox="0 0 1200 750" aria-hidden="true">
    <path d="M0 185 L1200 185 L1200 300 Q700 340 0 360 Z" fill="var(--navy)"/>
    <path d="M0 360 Q700 340 1200 300 L1200 315 Q700 352 0 372 Z" fill="var(--white)"/>
    <path d="M0 400 Q600 395 1200 330" fill="none" stroke="var(--navy)" stroke-width="5"/>
  </svg>

  <div class="layer faucet" role="img" aria-label="Chrome water faucet with a falling drop"></div>

  <header class="layer brand">
    <div class="brand-name">Marcotte Plumbing</div>
    <div class="brand-tagline">Gas | Water | Sewage</div>
  </header>

  <p class="layer promo-copy">
    Ask about our whole<br>
    <span class="highlight">Home water replacement package</span><br>
    and never worry about rust and corrosion<br>
    in your water lines again.
  </p>

  <ul class="layer services" style="list-style:none">
    <li class="service"><div class="service-image" role="img" aria-label="Tankless water heater" style="background:linear-gradient(#cfd6dc,#8c98a4)"></div><span class="service-label">Water<br>Heating</span></li>
    <li class="service"><div class="service-image" role="img" aria-label="Sewer manhole cover" style="background:linear-gradient(#4a4a4a,#1d1d1d)"></div><span class="service-label">Sewer<br>Repair</span></li>
    <li class="service"><div class="service-image" role="img" aria-label="Leaking copper pipe" style="background:linear-gradient(#d9a57c,#9a5b35)"></div><span class="service-label">Leakage<br>Repair</span></li>
    <li class="service"><div class="service-image" role="img" aria-label="Plumbing tools" style="background:linear-gradient(#e9ecef,#c2373a)"></div><span class="service-label">Re-<br>modelling</span></li>
  </ul>

  <div class="layer red-band"></div>

  <div class="layer plumber" role="img" aria-label="Smiling plumber in navy uniform and cap holding out a red pipe wrench"></div>

  <svg class="layer burst" viewBox="0 0 220 150" aria-hidden="true">
    <polygon fill="var(--red-bright)" points="220,75 177.6,87.4 205.3,112.5 159.5,108.9 165,140 128.1,121.4 110,150 91.9,121.4 55,140 60.5,108.9 14.7,112.5 42.4,87.4 0,75 42.4,62.6 14.7,37.5 60.5,41.1 55,10 91.9,28.6 110,0 128.1,28.6 165,10 159.5,41.1 205.3,37.5 177.6,62.6"/>
  </svg>
  <div class="layer burst-text">Free<br>Estimates</div>

  <div class="layer headline">
    <div class="headline-main">Need A Plumber?</div>
    <div class="headline-sub">Call NOW!</div>
  </div>

  <div class="layer license">License number<br>RKT 4291</div>

  <div class="layer contact">
    <div class="contact-phone">+1 985-555-0147</div>
    <div class="contact-address">52907 north elm ave. Cut Off, La. 70218</div>
  </div>
</main>
</body>
</html>
```